Upscale dog care facility need some marketing material

We offer a lot of services for dogs and their humans. We have a large indoor dog park, swimming pools, dog daycare and boarding, Pet CPR/First Aid classes and training. We love the trifold brochures where we can highlight all of our services (even a few pics of the facility) as well as give everyone information on our pricing and membership concepts. Will primarily be used for marketing to vets and local pet stores to help get the word out about our business.

```html
<!DOCTYPE html>
<html lang="en">
<head>
<meta charset="utf-8">
<title>Dog Care Trifold Brochure – Inside Spread</title>
<link href="https://fonts.googleapis.com/css2?family=Fredoka:wght@400;600;700&family=Montserrat:wght@400;500;600&display=swap" rel="stylesheet">
<style>
  :root {
    --page-bg: #ececec;
    --yellow: #f1e88f;
    --orange: #f29426;
    --orange-light: #f3b44e;
    --magenta: #b4146f;
    --teal: #2fb592;
    --teal-dark: #1e8f73;
    --white: #ffffff;
    --ink: #2b2b2b;
    --heading-font: "Fredoka", sans-serif;
    --body-font: "Montserrat", sans-serif;
  }
  * { margin: 0; padding: 0; box-sizing: border-box; }
  html, body { width: 1200px; height: 800px; overflow: hidden; }
  body { background: var(--page-bg); position: relative; font-family: var(--body-font); }

  .brochure {
    position: absolute; left: 100px; top: 12px;
    width: 1000px; height: 776px; overflow: hidden;
    box-shadow: 0 12px 30px rgba(0,0,0,.18);
  }
  .brochure__art { position: absolute; inset: 0; width: 1000px; height: 776px; }
  .brochure__text { position: absolute; inset: 0; }
  .abs { position: absolute; }

  /* Panel 1 – Why Us */
  .why-title {
    left: 36px; top: 300px;
    font-family: var(--heading-font); font-weight: 700;
    font-size: 40px; color: var(--magenta); line-height: 1;
  }
  .why-rule { left: 36px; top: 348px; width: 262px; height: 2px; background: var(--teal); }
  .why-copy {
    left: 36px; top: 360px; width: 272px;
    font-size: 11px; line-height: 1.4; color: var(--ink); font-weight: 500;
  }

  .quote { color: var(--white); font-size: 10.5px; line-height: 1.45; font-weight: 500; }
  .quote-mark {
    font-family: Georgia, serif; font-weight: 700;
    font-size: 44px; line-height: 1; color: var(--teal-dark);
  }
  .quote-name { color: var(--white); font-size: 10.5px; font-weight: 600; letter-spacing: .5px; }

  /* Panel 2 – Services */
  .services-title {
    left: 360px; top: 34px;
    font-family: var(--heading-font); font-weight: 700;
    font-size: 36px; color: var(--white); letter-spacing: .5px;
  }
  .service-name {
    font-family: var(--heading-font); font-weight: 400;
    font-size: 21px; line-height: 1.12; color: var(--white);
  }

  /* Panel 3 – Pricing */
  .pricing-title {
    left: 692px; top: 24px;
    font-family: var(--heading-font); font-weight: 700;
    font-size: 32px; line-height: 1.05; color: var(--white); letter-spacing: .5px;
  }
  .price-tag {
    width: 98px; height: 42px; border-radius: 8px;
    background: linear-gradient(180deg, var(--orange-light), var(--orange));
    color: var(--white); font-family: var(--heading-font); font-weight: 700;
    font-size: 30px; line-height: 42px; text-align: center;
  }
  .plan-name { font-family: var(--heading-font); font-weight: 600; font-size: 18px; color: var(--white); }
  .plan-copy { color: var(--white); font-size: 9.5px; line-height: 1.35; width: 280px; }
</style>
</head>
<body>
<div class="brochure">
  <svg class="brochure__art" viewBox="0 0 1000 776" xmlns="http://www.w3.org/2000/svg">
    <defs>
      <linearGradient id="orangePanel" x1="0" y1="0" x2="0" y2="1">
        <stop offset="0" stop-color="#f39a25"/>
        <stop offset="1" stop-color="#f3b453"/>
      </linearGradient>
      <linearGradient id="lawnTone" x1="0" y1="0" x2="1" y2="1">
        <stop offset="0" stop-color="#6aa337"/>
        <stop offset="1" stop-color="#4c8a28"/>
      </linearGradient>
      <linearGradient id="roomTone" x1="0" y1="0" x2="1" y2="1">
        <stop offset="0" stop-color="#eeeae4"/>
        <stop offset="1" stop-color="#c49a6a"/>
      </linearGradient>
    </defs>

    <!-- panel backgrounds -->
    <rect class="panel panel--why" x="0" y="0" width="334" height="776" fill="#f1e88f"/>
    <rect class="panel panel--services" x="333" y="0" width="334" height="776" fill="url(#orangePanel)"/>
    <rect class="panel panel--pricing" x="666" y="0" width="334" height="776" fill="#b4146f"/>

    <!-- teal wave band -->
    <path class="wave" fill="#2fb592"
      d="M0,575 C120,572 230,598 333,612 C430,624 520,570 590,510 C640,465 680,428 740,412 C820,392 920,382 1000,378 L1000,776 L0,776 Z"/>
    <path class="wave-stitch" fill="none" stroke="#ffffff" stroke-width="2" stroke-dasharray="6 5"
      d="M0,591 C120,588 230,614 333,628 C430,640 520,586 590,526 C640,481 680,444 740,428 C820,408 920,398 1000,394"/>

    <!-- panel 1 photo blob -->
    <g class="hero-photo" transform="translate(14,0) scale(0.92)">
      <path class="blob-outline" fill="none" stroke="#2fb592" stroke-width="2" stroke-dasharray="5 4"
        d="M60,60 C120,8 240,20 300,110 C345,180 340,270 300,300 C240,330 140,320 70,310 C20,300 8,240 16,170 C22,120 30,85 60,60 Z"/>
      <path class="photo" role="img" aria-label="Photo: puppy lying on its back on green grass"
        fill="url(#lawnTone)" stroke="#b4146f" stroke-width="8"
        d="M70,70 C125,25 235,38 288,118 C325,180 322,258 290,285 C235,310 140,300 78,292 C36,285 26,235 30,172 C34,125 42,95 70,70 Z"/>
    </g>

    <!-- panel 1 testimonial photo -->
    <circle role="img" aria-label="Photo: woman hugging a small white dog" cx="150" cy="604" r="50"
      fill="#e3d8cc" stroke="#b4146f" stroke-width="6"/>

    <!-- panel 2 service rules and photos -->
    <g class="service-rules" stroke="#ffffff" stroke-width="1.5" opacity=".85">
      <line x1="360" y1="88" x2="640" y2="80"/>
      <line x1="430" y1="185" x2="640" y2="180"/>
      <line x1="430" y1="275" x2="640" y2="270"/>
      <line x1="430" y1="365" x2="640" y2="360"/>
    </g>
    <circle role="img" aria-label="Photo: dogs playing in the indoor dog park" cx="390" cy="138" r="38" fill="#4f8a6e"/>
    <circle role="img" aria-label="Photo: dog swimming in a pool" cx="390" cy="228" r="38" fill="#2f74b5"/>
    <circle role="img" aria-label="Photo: dogs in the daycare room" cx="390" cy="318" r="38" fill="#c9c2b6"/>
    <circle role="img" aria-label="Photo: dog training session outdoors" cx="390" cy="408" r="38" fill="#a9b58c"/>

    <circle role="img" aria-label="Photo: smiling woman holding a small fluffy dog" cx="540" cy="540" r="50"
      fill="#7aa04e" stroke="#b4146f" stroke-width="6"/>

    <!-- panel 3 -->
    <line x1="692" y1="104" x2="980" y2="94" stroke="#ffffff" stroke-width="1.5" opacity=".85"/>
    <path class="blob-outline" fill="none" stroke="#ffffff" stroke-width="2" stroke-dasharray="6 5"
      d="M720,440 C780,385 900,392 960,420 C1000,440 998,530 990,610 C985,700 960,760 880,765 C800,770 720,760 700,700 C685,640 680,500 720,440 Z"/>
    <path class="photo" role="img" aria-label="Photo: woman giving a high five to a golden retriever at home"
      fill="url(#roomTone)" stroke="#f29426" stroke-width="8"
      d="M735,452 C790,405 895,410 948,434 C982,452 982,535 976,610 C970,690 950,742 878,748 C805,752 738,744 720,692 C706,640 702,500 735,452 Z"/>
  </svg>

  <div class="brochure__text">
    <!-- panel 1 -->
    <h2 class="abs why-title">Why Us</h2>
    <div class="abs why-rule"></div>
    <p class="abs why-copy">Lorem ipsum dolor sit amet, consectetur adipiscing elit, sed do eiusmod tempor incididunt ut labore et dolore magna aliqua. Ut enim ad minim veniam, quis nostrud exercitation ullamco laboris nisi ut aliquip ex ea commodo consequat. Duis aute irure dolor in reprehenderit in voluptate velit esse cillum dolore eu fugiat nulla pariatur.</p>

    <span class="abs quote-mark" style="left:36px;top:660px;">&ldquo;</span>
    <p class="abs quote" style="left:40px;top:690px;width:270px;">sed do eiusmod tempor incididunt ut labore et dolore magna aliqua. Ut enim ad minim veniam, quis nostrud exercitation ullamco laboris nisi ut aliquip ex ea commodo consequat.</p>
    <span class="abs quote-name" style="left:210px;top:752px;">JOHAN DOE</span>
    <span class="abs quote-mark" style="left:282px;top:740px;">&rdquo;</span>

    <!-- panel 2 -->
    <h2 class="abs services-title">OUR SERVICES</h2>
    <p class="abs service-name" style="left:440px;top:114px;">Large Indoor<br>Dog Park</p>
    <p class="abs service-name" style="left:440px;top:204px;">Swimming<br>Pools</p>
    <p class="abs service-name" style="left:440px;top:294px;">Dog Daycare<br>and Boarding</p>
    <p class="abs service-name" style="left:440px;top:382px;">Pet Cpr/First Aid<br>Classes<br>And Training</p>

    <span class="abs quote-mark" style="left:358px;top:628px;">&ldquo;</span>
    <p class="abs quote" style="left:362px;top:660px;width:280px;">sed do eiusmod tempor incididunt ut labore et dolore magna aliqua. Ut enim ad minim veniam, quis nostrud exercitation ullamco laboris nisi ut aliquip ex ea commodo consequat.</p>
    <span class="abs quote-name" style="left:556px;top:726px;">JOHAN DOE</span>
    <span class="abs quote-mark" style="left:626px;top:714px;">&rdquo;</span>

    <!-- panel 3 -->
    <h2 class="abs pricing-title">PRICING &amp;<br>MEMBERSHIP</h2>

    <div class="abs price-tag" style="left:692px;top:120px;">$199</div>
    <span class="abs plan-name" style="left:802px;top:116px;">Lorem ipsum</span>
    <p class="abs plan-copy" style="left:692px;top:166px;">sed do eiusmod tempor incididunt ut labore et dolore magna aliqua. Ut enim ad minim veniam.</p>

    <div class="abs price-tag" style="left:692px;top:194px;">$199</div>
    <span class="abs plan-name" style="left:802px;top:190px;">Lorem ipsum</span>
    <p class="abs plan-copy" style="left:692px;top:240px;">sed do eiusmod tempor incididunt ut labore et dolore magna aliqua. Ut enim ad minim veniam.</p>

    <div class="abs price-tag" style="left:692px;top:268px;">$199</div>
    <span class="abs plan-name" style="left:802px;top:264px;">Lorem ipsum</span>
    <p class="abs plan-copy" style="left:692px;top:314px;">sed do eiusmod tempor incididunt ut labore et dolore magna aliqua. Ut enim ad minim veniam.</p>
  </div>
</div>
</body>
</html>
```